Brownie Snack Packaging

Design the film wrapper packaging for a brownie snack. It needs to be cohesive with our existing product line (please review attached photos), but still differentiated from it to avoid customer confusion.
Brief is outlined in the images attached. Please review prior to submitting designs. All designs should have the iridescent white pearl packaging color, with the text:
High Protein Brownie
10g Protein
Vegan
Gluten-Free
No Added Sugars
We would like to see designs with square packaging with a mouth-watering brownie image being the most prominent. Logo of brand "ORUNE" should be in upper right corner.
Note: we have another product line of cashew butter sachets that are pink, blue, & chocolate - I'm attaching those for reference so you can design these brownies to look somewhat related to the cashew butters.
Look and feel
Each slider illustrates characteristics of the customer's brand and the style your logo design should communicate.

```html
<!DOCTYPE html>
<html lang="en">
<head>
<meta charset="utf-8">
<title>ORUNE High Protein Brownie – Wrapper Front</title>
<link rel="stylesheet" href="https://fonts.googleapis.com/css2?family=Playfair+Display:wght@900&family=Roboto+Condensed:wght@400&family=Josefin+Sans:wght@400&display=swap">
<style>
  :root {
    --stage: #232124;
    --pearl-white: #f4f8f8;
    --pearl-cyan: #a8dde6;
    --pearl-pink: #e6c6e6;
    --pearl-lilac: #cfc4ee;
    --pearl-mint: #c8efe4;
    --ink: #0b0b0b;
    --brand-gold: #a4895d;
    --badge-text: #a9e3e2;
    --choc-dark: #2a1610;
    --choc-mid: #5a3322;
  }
  * { margin: 0; padding: 0; box-sizing: border-box; }
  html, body { width: 764px; height: 1200px; overflow: hidden; background: var(--stage); }
  .canvas { position: relative; width: 764px; height: 1200px; }

  .wrapper-front {
    position: absolute;
    left: 72px; top: 249px;
    width: 620px; height: 702px;
    overflow: hidden;
    background:
      radial-gradient(ellipse 40% 22% at 20% 12%, rgba(230,198,230,.8), transparent 70%),
      radial-gradient(ellipse 35% 25% at 70% 30%, rgba(255,255,255,.95), transparent 70%),
      radial-gradient(ellipse 45% 30% at 10% 55%, rgba(168,221,230,.9), transparent 70%),
      radial-gradient(ellipse 40% 25% at 85% 62%, rgba(207,196,238,.8), transparent 70%),
      radial-gradient(ellipse 50% 22% at 30% 85%, rgba(230,198,230,.85), transparent 70%),
      radial-gradient(ellipse 40% 20% at 85% 92%, rgba(200,239,228,.85), transparent 70%),
      radial-gradient(ellipse 30% 18% at 55% 8%, rgba(200,239,228,.7), transparent 70%),
      linear-gradient(160deg, var(--pearl-cyan), var(--pearl-white) 40%, var(--pearl-lilac) 70%, var(--pearl-cyan));
  }

  .brand-name {
    position: absolute;
    right: 39px; top: 42px;
    font-family: "Josefin Sans", sans-serif;
    font-weight: 400;
    font-size: 66px;
    letter-spacing: 3px;
    color: var(--brand-gold);
    line-height: 1;
  }

  .product-photo {
    position: absolute;
    left: 37px; top: 151px;
    width: 558px; height: 317px;
    background: radial-gradient(ellipse 50% 45% at 50% 45%, var(--choc-mid), var(--choc-dark) 60%, transparent 72%);
  }

  .product-title {
    font-family: "Playfair Display", serif;
    font-weight: 900;
    color: var(--ink);
    font-variant-numeric: lining-nums;
  }
  .title-kicker, .title-main {
    position: absolute;
    left: 0; right: 0;
    text-align: center;
    white-space: nowrap;
  }
  .title-kicker {
    top: 476px;
    font-size: 37px;
    line-height: 37px;
    letter-spacing: -.5px;
    padding-left: 14px;
  }
  .title-main {
    top: 484px;
    font-size: 92px;
    line-height: 92px;
    letter-spacing: -3px;
  }

  .protein-badge {
    position: absolute;
    left: 113px; top: 576px;
    width: 399px; height: 47px;
    background: var(--ink);
    color: var(--badge-text);
    font-family: "Playfair Display", serif;
    font-weight: 900;
    font-size: 34px;
    line-height: 47px;
    text-align: center;
    font-variant-numeric: lining-nums;
  }

  .claims {
    position: absolute;
    left: 0; right: 0; top: 630px;
    text-align: center;
    font-family: "Roboto Condensed", sans-serif;
    font-size: 15.5px;
    line-height: 20px;
    color: var(--ink);
  }
  .claims .divider { display: inline-block; width: 2px; height: 14px; background: var(--ink); margin: 0 7px; vertical-align: -2px; }

  .net-weight {
    position: absolute;
    left: 0; right: 0; top: 659px;
    text-align: center;
    font-family: "Roboto Condensed", sans-serif;
    font-size: 14.5px;
    line-height: 20px;
    color: var(--ink);
  }
</style>
</head>
<body>
<main class="canvas">
  <section class="wrapper-front">
    <div class="brand-name">ORUNE</div>
    <div class="product-photo" role="img" aria-label="Photo of a chocolate brownie drizzled with glossy chocolate sauce"></div>
    <h1 class="product-title">
      <span class="title-kicker">High Protein</span>
      <span class="title-main">Brownie</span>
    </h1>
    <div class="protein-badge">10g Protein</div>
    <p class="claims">No Added Sugars<span class="divider"></span>Vegan<span class="divider"></span>Gluten Free</p>
    <p class="net-weight">Net wt 2 oz (50g)</p>
  </section>
</main>
</body>
</html>
```